KB Rubbish Removal Business Card

Hey,
I need a double sided business card designed for a rubbish removal business based in Australia. Logo is already chosen, similar colours preferred for both sides of the business card.

Details to include:

Front:

KB Rubbish Removal
Darren Holloway
Managing Director
Mobile: 0471 902 146
Email: darren@kbrubbishremoval.com.au
Website: kbrubbishremoval.com.au

Rear:

How did we do?
kbrubbishremoval.com.au/review

```html
<!DOCTYPE html>
<html lang="en">
<head>
<meta charset="UTF-8">
<title>KB Rubbish Removal – Business Card</title>
<link href="https://fonts.googleapis.com/css2?family=Lato:wght@400;700;900&display=swap" rel="stylesheet">
<style>
  :root {
    --page: #e4e4e4;
    --card: #1e1f21;
    --green: #3db54a;
    --green-deep: #1f8f3e;
    --white: #ffffff;
    --muted: #d8d8d8;
  }
  * { margin: 0; padding: 0; box-sizing: border-box; }
  html, body { width: 1200px; height: 1200px; overflow: hidden; }
  body {
    background: var(--page);
    font-family: "Lato", Arial, sans-serif;
    position: relative;
  }
  .card {
    position: absolute;
    width: 706px;
    height: 400px;
    background: var(--card);
    overflow: hidden;
  }
  .card-front { left: 242px; top: 150px; }
  .card-back { left: 240px; top: 620px; }

  /* Front */
  .brand-name {
    position: absolute;
    left: 46px;
    top: 74px;
    font-size: 32px;
    line-height: 1.2;
    font-weight: 900;
    color: var(--green);
    white-space: nowrap;
  }
  .name-band {
    position: absolute;
    left: 0;
    top: 170px;
    width: 425px;
    height: 63px;
    background: linear-gradient(90deg, var(--green) 0%, var(--green) 18%, rgba(61,181,74,0.35) 55%, rgba(30,31,33,0) 100%);
  }
  .person-name {
    position: absolute;
    left: 49px;
    top: 173px;
    font-size: 28px;
    line-height: 1;
    font-weight: 700;
    color: var(--white);
    white-space: nowrap;
  }
  .person-role {
    position: absolute;
    left: 49px;
    top: 204px;
    font-size: 19px;
    line-height: 1;
    font-weight: 400;
    color: var(--white);
    white-space: nowrap;
  }
  .contact-list {
    position: absolute;
    left: 48px;
    top: 284px;
    list-style: none;
  }
  .contact-item {
    display: flex;
    align-items: center;
    height: 26.5px;
    font-size: 20px;
    color: var(--white);
    white-space: nowrap;
  }
  .contact-icon {
    width: 14px;
    height: 14px;
    margin-right: 12px;
    fill: var(--green);
  }
  .emblem-front {
    position: absolute;
    left: 360px;
    top: 51px;
    width: 298px;
    height: 298px;
    border-radius: 50%;
    background: radial-gradient(circle at 40% 35%, rgba(61,181,74,0.22), rgba(31,143,62,0.10));
  }

  /* Back */
  .back-texture {
    position: absolute;
    inset: 0;
    background: linear-gradient(100deg, #2a2b2d 0%, #232426 45%, #18191a 100%);
  }
  .emblem-back {
    position: absolute;
    left: 296px;
    top: 110px;
    width: 114px;
    height: 114px;
    border-radius: 50%;
    background: linear-gradient(135deg, var(--green), var(--green-deep));
  }
  .brand-name-back {
    position: absolute;
    left: 0;
    right: 0;
    top: 238px;
    text-align: center;
    font-size: 34px;
    line-height: 1.2;
    font-weight: 900;
    color: var(--green);
    white-space: nowrap;
  }
  .review-prompt {
    position: absolute;
    left: 0;
    right: 0;
    top: 300px;
    text-align: center;
    font-size: 17px;
    line-height: 1.2;
    font-weight: 700;
    color: var(--white);
    white-space: nowrap;
  }
  .review-link {
    position: absolute;
    left: 0;
    right: 0;
    top: 326px;
    text-align: center;
    font-size: 16px;
    line-height: 1.2;
    font-weight: 400;
    color: var(--muted);
    white-space: nowrap;
  }
</style>
</head>
<body>

  <section class="card card-front">
    <div class="emblem-front"></div>
    <div class="brand-name">KB Rubbish Removal</div>
    <div class="name-band"></div>
    <div class="person-name">Darren Holloway</div>
    <div class="person-role">Managing Director</div>
    <ul class="contact-list">
      <li class="contact-item">
        <svg class="contact-icon" viewBox="0 0 24 24" aria-hidden="true"><path d="M6.6 10.8a15.1 15.1 0 0 0 6.6 6.6l2.2-2.2a1 1 0 0 1 1-.25 11.4 11.4 0 0 0 3.6.57 1 1 0 0 1 1 1V20a1 1 0 0 1-1 1A17 17 0 0 1 3 4a1 1 0 0 1 1-1h3.5a1 1 0 0 1 1 1c0 1.25.2 2.45.57 3.57a1 1 0 0 1-.25 1z"/></svg>
        0471 902 146
      </li>
      <li class="contact-item">
        <svg class="contact-icon" viewBox="0 0 24 24" aria-hidden="true"><path d="M12 2a10 10 0 1 0 0 20 10 10 0 0 0 0-20zm-1 17.9A8 8 0 0 1 4.1 10.6L9 15.5v1a2 2 0 0 0 2 2zm6.9-2.5A2 2 0 0 0 16 16h-1v-3a1 1 0 0 0-1-1H8v-2h2a1 1 0 0 0 1-1V7h2a2 2 0 0 0 2-2v-.4a8 8 0 0 1 2.9 12.8z"/></svg>
        kbrubbishremoval.com.au
      </li>
      <li class="contact-item">
        <svg class="contact-icon" viewBox="0 0 24 24" aria-hidden="true"><path d="M2 5h20v2l-10 6L2 7zm0 4.3 10 6 10-6V19H2z"/></svg>
        darren@kbrubbishremoval.com.au
      </li>
    </ul>
  </section>

  <section class="card card-back">
    <div class="back-texture" role="img" aria-label="Faint repeating brand pattern across the dark card background"></div>
    <div class="emblem-back"></div>
    <div class="brand-name-back">KB Rubbish Removal</div>
    <div class="review-prompt">How did we do?</div>
    <div class="review-link">kbrubbishremoval.com.au/review</div>
  </section>

</body>
</html>
```